BRAVO Tea & Herbal Tea Packaging Labels

We are seeking new consistent front label designs that we can use for both retail and wholesale packaging purposes:

BRAVO PHILOSOPHY

BRAVO provides a selection of ‘energy enhanced’ signature infusion blends that taste great while assisting a person deeply on several levels – emotional, mental, physical and spiritual.

We source quality ingredients and specifically use certified organic, spray free and wildcrafted ingredients for our herbal blends.

BRAVO’s PRODUCT RANGE

A. 6 standard signature herbal blends (standard range)
B. 2 seasonal blends - which change every quarter (1 x herbal blend, 1 x tea-based blend)
C. selection of teas – black, green, white, oolong (which vary in type and number)
D. custom and limited edition blends – herbal and teas
E. tea drinking accessories.

11 LABELS ARE REQUIRED

Labels 1-8 for Herbal Blends (to be denoted by an accent of SILVER)
Labels 9-10 for Teas (to be denoted by an accent of GOLD)
Label 11 for Accessories

LABEL SIZE

Current front label dimensions: 63.5 x 72mm long – willing to look at alternate label size
Current ‘usable area’ of smallest resealable bag: 110 x 130mm long

** PLEASE SEE ATTACHED WORD DOC FOR COMPLETE SPECIFICATION - PLEASE READ BEFORE COMMENCING ANY WORK **
Updates

hi,

forgot to include an attachment of the current labels for herbal teas that are used... here is a link to the PDF.

http://files.quorvanshare.com/u/48213675/BRAVO-Herbal-Labels.pdf

thanks Derek

Hi,

please note we have attached a jpg of the packaging the label goes onto... it is in the attached files in the brief - called packaging.

thanks Derek

Hi, we've uploaded some pics of the current packaging to give you a sense of the packaging we are using and the space on the front pack to work with.

many thanks.

Target Market(s)

Women and men aged 30-55 with an interest in natural products, emotional/spiritual wellbeing and support.

BRAVO DISTRIBUTION

Online store for retail sales,
Cafes for food service,
Practitioner (naturopaths, massage therapists, energy healers) clinics and stores.

Industry/Entity Type

Retail

Requirements
Must have
• Each label should have:
• Current logo and tagline;
• Website name;
• Silver accent for herbal range labels;
• Gold accent for tea range labels;
• Colour-coding for the 6 signature herbals.
• ** PLEASE SEE ATTACHED WORD DOC FOR COMPLETE SPECIFICATION - PLEASE READ BEFORE COMMENCING ANY WORK **
Nice to have
• Mrs Eaves font for text (to match logo font type)

```html
<!DOCTYPE html>
<html lang="en">
<head>
<meta charset="utf-8">
<title>BRAVO Infusions – Mint Haven Label</title>
<link rel="stylesheet" href="https://fonts.googleapis.com/css2?family=Cormorant+Garamond:ital,wght@0,500;0,600;1,500&family=Great+Vibes&display=swap">
<style>
  :root {
    --frame-grey: #a6a7a9;
    --sky-blue: #1ca2e3;
    --sky-stripe: #4fb6ea;
    --sky-glow: rgba(255, 255, 255, 0.35);
    --teal: #00b4a5;
    --mint: #b3dfcb;
    --ink: #1d1d1d;
    --organic-green: #0d6a3b;
    --white: #ffffff;
    --serif: "Cormorant Garamond", "Times New Roman", serif;
    --script: "Great Vibes", cursive;
  }
  * { margin: 0; padding: 0; box-sizing: border-box; }
  html, body {
    width: 1200px;
    height: 900px;
    overflow: hidden;
    background: var(--white);
  }
  .canvas { position: relative; width: 1200px; height: 900px; }
  /* Label is built upright, then turned to run down the page */
  .label {
    position: absolute;
    left: 169px;
    top: -54px;
    width: 836px;
    height: 988px;
    background: var(--frame-grey);
    transform: rotate(90deg);
    transform-origin: 50% 50%;
    color: var(--white);
    font-family: var(--serif);
  }
  .label__field {
    position: absolute;
    left: 24px;
    top: 24px;
    width: 788px;
    height: 940px;
    background:
      radial-gradient(ellipse at 50% 45%, var(--sky-glow), transparent 60%),
      repeating-linear-gradient(90deg, var(--sky-blue) 0 7px, var(--sky-stripe) 7px 13px);
  }
  .band {
    position: absolute;
    left: 0;
    width: 836px;
    display: flex;
    align-items: center;
    justify-content: center;
  }
  .band--name { top: 243px; height: 148px; background: var(--teal); }
  .band--tagline { top: 400px; height: 75px; background: var(--mint); }

  .brand {
    position: absolute;
    left: 160px;
    top: 70px;
    display: flex;
    align-items: baseline;
    white-space: nowrap;
  }
  .brand__name {
    font-size: 100px;
    font-weight: 500;
    letter-spacing: 3px;
    line-height: 1;
  }
  .brand__dot {
    width: 40px;
    height: 40px;
    border-radius: 50%;
    border: 3px solid var(--white);
    margin: 0 10px 0 14px;
    align-self: center;
  }
  .brand__range {
    font-size: 42px;
    font-style: italic;
    letter-spacing: 1px;
    line-height: 1;
  }
  .product-name {
    font-family: var(--script);
    font-size: 112px;
    font-weight: 400;
    line-height: 1;
    color: var(--white);
    padding-top: 12px;
    white-space: nowrap;
  }
  .tagline {
    font-family: var(--script);
    font-size: 40px;
    color: var(--ink);
    -webkit-text-stroke: 0.6px var(--ink);
    white-space: nowrap;
  }
  .description {
    position: absolute;
    left: 0;
    width: 836px;
    top: 520px;
    text-align: center;
    font-size: 25px;
    line-height: 29px;
    font-weight: 500;
    white-space: nowrap;
  }
  .certified {
    position: absolute;
    left: 0;
    width: 836px;
    top: 672px;
    text-align: center;
    font-style: italic;
    font-size: 28px;
    color: var(--organic-green);
  }
  .serving {
    position: absolute;
    left: 0;
    width: 836px;
    top: 748px;
    text-align: center;
    font-style: italic;
    font-size: 21px;
    line-height: 24px;
    white-space: nowrap;
  }
  .website {
    position: absolute;
    left: 78px;
    top: 866px;
    font-style: italic;
    font-size: 34px;
    white-space: nowrap;
  }
  .signoff {
    position: absolute;
    left: 452px;
    top: 866px;
    font-style: italic;
    font-size: 34px;
    white-space: nowrap;
  }
  .cup-art {
    position: absolute;
    left: 672px;
    top: 868px;
    width: 96px;
    height: 54px;
    border-radius: 6px;
    background: radial-gradient(circle, rgba(255,255,255,0.55), rgba(255,255,255,0.15));
  }
</style>
</head>
<body>
<main class="canvas">
  <section class="label" aria-label="BRAVO Infusions Mint Haven tea label">
    <div class="label__field"></div>

    <header class="brand">
      <span class="brand__name">BRAVO</span>
      <span class="brand__dot" aria-hidden="true"></span>
      <span class="brand__range">infusions</span>
    </header>

    <div class="band band--name">
      <h1 class="product-name">Mint Haven</h1>
    </div>
    <div class="band band--tagline">
      <p class="tagline">Refreshes, clarifies, internal body hug</p>
    </div>

    <p class="description">For those who love a refreshing mint taste, the gentle<br>flavour of spearmint combined with lavender,<br>rose petals and echinacea delight the senses and give<br>what we regard as an “internal body hug”.</p>

    <p class="certified">Certified Organic ingredients</p>

    <p class="serving">Serving: for optimum flavour pour freshly boiled water over<br>one generous teaspoon per cup and steep 3–5 mins</p>

    <p class="website">www.bravo.com.au</p>
    <p class="signoff">calm in each sip</p>
    <div class="cup-art" role="img" aria-label="Line drawing of a teacup with small daisies"></div>
  </section>
</main>
</body>
</html>
```